Infographic Table of AI Pricing Options for LinkedIn post

Turn this table (in the powerpoint slide attached) into an attractively formatted infographic table for Solqarin (www.solqarin.com).
This will be an infographic displayed on a linkedin post from a consultant from Solqarin.
Try to keep it on brand with Solqarin look and feel.

Target Market(s)

Tech and SaaS CEOs and Founders; Private Equity and Venture Capital employees

Industry/Entity Type

Management Consulting

Colors
0054AA
0677BA
7BADD7
CADEEF
E8F1F8

```html
<!DOCTYPE html>
<html lang="en">
<head>
<meta charset="utf-8">
<title>Solqarin – Challenges of GenAI Monetization</title>
<link rel="stylesheet" href="https://fonts.googleapis.com/css2?family=Montserrat:wght@500;600;700;800&display=swap">
<style>
  :root{
    --navy-frame:#14273f;
    --ink:#1d3047;
    --ink-dark:#1a1f26;
    --brand-blue:#0054AA;
    --brand-mid:#0677BA;
    --brand-sky:#7BADD7;
    --brand-pale:#CADEEF;
    --brand-mist:#E8F1F8;
    --teal-band:#5EC4C2;
    --white:#ffffff;
    --letter-a:#1fcf86;
    --letter-b:#17c47c;
    --letter-c:#12b3c0;
    --letter-d:#f2673f;
  }
  *{margin:0;padding:0;box-sizing:border-box}
  html,body{width:1200px;height:958px;overflow:hidden;background:var(--navy-frame)}
  body{font-family:"Montserrat",sans-serif;color:var(--ink);position:relative}
  .sheet{position:absolute;left:43px;top:43px;width:1114px;height:872px;background:var(--white);overflow:hidden}
  .sheet > *{position:absolute}

  .brand{left:15px;top:17px;display:flex;align-items:center;gap:10px}
  .brand-square{width:44px;height:44px;border-radius:6px;background:var(--brand-mid)}
  .brand-name{font-size:33px;font-weight:500;color:var(--ink-dark);letter-spacing:.3px}

  .title{left:42px;top:113px;font-size:28.5px;line-height:33px;font-weight:700;color:var(--brand-blue)}

  .model-panel{left:275px;top:73px;width:839px;height:207px;background:var(--brand-mist);border-radius:3px}
  .ribbon{top:55px;width:96px;height:108px}
  .model-name{top:176px;width:200px;text-align:center;font-size:23px;line-height:27px;font-weight:700;color:var(--ink);letter-spacing:0;white-space:nowrap}
  .model-letter{top:232px;width:80px;height:47px;overflow:hidden;text-align:center;font-size:56px;line-height:56px;font-weight:800}

  .band{left:0;width:1114px}
  .band-description{top:310px;height:123px;background:var(--teal-band)}
  .band-examples{top:433px;height:147px;background:var(--white)}
  .band-pros{top:581px;height:122px;background:var(--brand-sky)}
  .band-cons{top:722px;height:123px;background:var(--brand-pale)}

  .cell{position:absolute;top:0;bottom:0;display:flex;align-items:center;font-size:12px;line-height:14.4px;font-weight:700;letter-spacing:.45px;color:var(--ink);text-transform:uppercase}
  .row-label{left:45px;width:88px;justify-content:center;flex-direction:column;text-align:center;font-size:12px}
  .row-label svg{margin-bottom:6px}

  .bullets{list-style:none}
  .bullets li{position:relative;padding-left:8px}
  .bullets li::before{content:"";position:absolute;left:0;top:6px;width:3px;height:3px;background:var(--ink)}

  .example-stack{flex-direction:column;align-items:flex-start;justify-content:center;gap:26px;text-transform:none}
  .example{display:flex;align-items:center;gap:8px;font-size:19px;font-weight:700;color:var(--ink-dark);letter-spacing:0}
  .mark-square{width:36px;height:36px;border-radius:7px;background:#1aa383}
  .mark-circle{width:22px;height:22px;border-radius:50%}
  .example-note{font-size:11.5px;font-weight:700;color:var(--ink-dark);letter-spacing:.3px}
</style>
</head>
<body>
<main class="sheet">
  <div class="brand">
    <span class="brand-square"></span>
    <span class="brand-name">solqarin</span>
  </div>

  <h1 class="title">Challenges<br>Of Genai<br>Monetization</h1>

  <div class="model-panel"></div>

  <!-- Model A -->
  <svg class="ribbon" style="left:340px" viewBox="0 0 96 108" aria-hidden="true">
    <defs><linearGradient id="ga" x1="0" y1="0" x2="0" y2="1"><stop offset="0" stop-color="#1ec8c9"/><stop offset="1" stop-color="#30e197"/></linearGradient></defs>
    <polygon points="0,18 9,0 9,18" fill="#158f86"/><polygon points="96,18 87,0 87,18" fill="#158f86"/>
    <path d="M9 0H87V92L48 108L9 92Z" fill="url(#ga)"/>
    <g fill="none" stroke="#fff" stroke-width="1.3"><rect x="34" y="30" width="28" height="36" rx="2"/><path d="M39 38h18M39 43h18M39 48h12M39 53h10"/><circle cx="56" cy="58" r="5"/></g>
  </svg>
  <div class="model-name" style="left:290px">USER<br>LICENSES</div>
  <div class="model-letter" style="left:348px;color:var(--letter-a)">A</div>

  <!-- Model B -->
  <svg class="ribbon" style="left:544px" viewBox="0 0 96 108" aria-hidden="true">
    <defs><linearGradient id="gb" x1="0" y1="0" x2="0" y2="1"><stop offset="0" stop-color="#8d84df"/><stop offset="1" stop-color="#c47bd6"/></linearGradient></defs>
    <polygon points="0,18 9,0 9,18" fill="#6a5aa8"/><polygon points="96,18 87,0 87,18" fill="#6a5aa8"/>
    <path d="M9 0H87V92L48 108L9 92Z" fill="url(#gb)"/>
    <g fill="none" stroke="#fff" stroke-width="1.3"><rect x="25" y="42" width="40" height="16" rx="5"/><circle cx="70" cy="50" r="4"/></g>
    <g fill="#fff"><circle cx="33" cy="50" r="1.6"/><circle cx="40" cy="50" r="1.6"/><circle cx="47" cy="50" r="1.6"/><circle cx="54" cy="50" r="1.6"/></g>
  </svg>
  <div class="model-name" style="left:495px">USER-BASED<br>TOKEN</div>
  <div class="model-letter" style="left:551px;color:var(--letter-b)">B</div>

  <!-- Model C -->
  <svg class="ribbon" style="left:749px" viewBox="0 0 96 108" aria-hidden="true">
    <defs><linearGradient id="gc" x1="0" y1="0" x2="0" y2="1"><stop offset="0" stop-color="#3ba1e6"/><stop offset="1" stop-color="#2cc3cf"/></linearGradient></defs>
    <polygon points="0,18 9,0 9,18" fill="#2479b0"/><polygon points="96,18 87,0 87,18" fill="#2479b0"/>
    <path d="M9 0H87V92L48 108L9 92Z" fill="url(#gc)"/>
    <g fill="none" stroke="#fff" stroke-width="1.3"><circle cx="50" cy="44" r="13"/><circle cx="50" cy="44" r="8"/><circle cx="50" cy="44" r="3"/><path d="M30 74L50 54L56 60L68 46M62 46h6v6"/></g>
  </svg>
  <div class="model-name" style="left:704px">OUTCOME-<br>BASED</div>
  <div class="model-letter" style="left:760px;color:var(--letter-c)">C</div>

  <!-- Model D -->
  <svg class="ribbon" style="left:953px" viewBox="0 0 96 108" aria-hidden="true">
    <defs><linearGradient id="gd" x1="0" y1="0" x2="0" y2="1"><stop offset="0" stop-color="#ee6a66"/><stop offset="1" stop-color="#ff905e"/></linearGradient></defs>
    <polygon points="0,18 9,0 9,18" fill="#b94a48"/><polygon points="96,18 87,0 87,18" fill="#b94a48"/>
    <path d="M9 0H87V92L48 108L9 92Z" fill="url(#gd)"/>
    <g fill="none" stroke="#fff" stroke-width="1.3"><path d="M48 32L66 42L48 52L30 42Z"/><path d="M30 48L48 58L66 48"/><path d="M30 54L48 64L66 54"/></g>
  </svg>
  <div class="model-name" style="left:908px">USAGE-TIERED<br>LICENSES</div>
  <div class="model-letter" style="left:966px;color:var(--letter-d)">D</div>

  <!-- Description -->
  <section class="band band-description">
    <div class="cell row-label">DESCRIPTION</div>
    <div class="cell" style="left:175px">Charge a flat<br>price for a user<br>to have access to<br>the functionality</div>
    <div class="cell" style="left:409px">Purchase blocks of<br>tokens that can be<br>spend on<br>usage/work of the<br>AI functionality</div>
    <div class="cell" style="left:612px">Pay for the<br>outcomes of<br>the GenAI<br>functionality</div>
    <div class="cell" style="left:828px">Offer different<br>user licenses<br>with different<br>usage capacities</div>
  </section>

  <!-- Examples -->
  <section class="band band-examples">
    <div class="cell row-label">EXAMPLES</div>
    <div class="cell example-stack" style="left:175px">
      <span class="example"><span class="mark-square"></span>Parlora</span>
      <span class="example"><span class="mark-circle" style="background:#c264d6"></span>Wingmate</span>
    </div>
    <div class="cell example-stack" style="left:412px">
      <span class="example"><span class="mark-circle" style="background:var(--ink-dark)"></span>Tokenwell</span>
      <span class="example" style="font-size:15px"><span class="mark-circle" style="background:#4a86e8"></span>Lenscape API</span>
    </div>
    <div class="cell example-stack" style="left:617px">
      <span class="example"><span class="mark-circle" style="background:#0f3a3f"></span>Ticketra</span>
      <span class="example"><span class="mark-circle" style="background:#3d5af1"></span>Disputo</span>
    </div>
    <div class="cell example-stack" style="left:832px;gap:20px">
      <span class="example"><span class="mark-square"></span>Parlora</span>
      <span class="example-note">kinda...</span>
    </div>
  </section>

  <!-- Pros -->
  <section class="band band-pros">
    <div class="cell row-label">
      <svg width="40" height="40" viewBox="0 0 40 40" aria-hidden="true"><circle cx="20" cy="20" r="18" fill="none" stroke="var(--brand-mist)" stroke-width="3"/><path d="M12 20l6 6 11-12" fill="none" stroke="var(--brand-mist)" stroke-width="3.5" stroke-linecap="round" stroke-linejoin="round"/></svg>
      PROS
    </div>
    <div class="cell" style="left:175px">Simple and easily<br>understood</div>
    <ul class="cell bullets" style="left:417px;flex-direction:column;justify-content:center;align-items:flex-start">
      <li>Covers costs at all<br>scales of usage</li>
      <li>Tokens help with<br>predictability issues</li>
    </ul>
    <div class="cell" style="left:630px">Potentially<br>highly<br>value-aligned</div>
    <ul class="cell bullets" style="left:835px;flex-direction:column;justify-content:center;align-items:flex-start">
      <li>Value aligned</li>
      <li>Simple &amp;<br>predictable</li>
      <li>Natural<br>upsell path</li>
      <li>Low barrier<br>to adoption</li>
    </ul>
  </section>

  <!-- Cons -->
  <section class="band band-cons">
    <div class="cell row-label">
      <svg width="40" height="40" viewBox="0 0 40 40" aria-hidden="true"><circle cx="20" cy="20" r="18" fill="none" stroke="var(--brand-sky)" stroke-width="3"/><path d="M13 13l14 14M27 13L13 27" stroke="var(--brand-sky)" stroke-width="3.5" stroke-linecap="round"/></svg>
      CONS
    </div>
    <ul class="cell bullets" style="left:182px;flex-direction:column;justify-content:center;align-items:flex-start">
      <li>High price limits adoption</li>
      <li>Not tightly value aligned</li>
      <li>Risky if fair usage<br>restriction is not placed<br>on</li>
      <li>Upsell dependent on<br>wider adoption</li>
    </ul>
    <ul class="cell bullets" style="left:417px;flex-direction:column;justify-content:center;align-items:flex-start">
      <li>Not tightly value<br>aligned (value may<br>not increase<br>linearly with usage)</li>
      <li>Not ARR</li>
    </ul>
    <ul class="cell bullets" style="left:620px;flex-direction:column;justify-content:center;align-items:flex-start">
      <li>Delayed revenue<br>realization</li>
      <li>Not ARR</li>
      <li>Tough to find the<br>right metric</li>
    </ul>
    <ul class="cell bullets" style="left:835px;flex-direction:column;justify-content:center;align-items:flex-start">
      <li>Limit on the<br>number of<br>tiers</li>
    </ul>
  </section>
</main>
</body>
</html>
```